Opening Soon Hoarding Design for Retail Footwear Chain

TREVALLO is a retail footwear chain operating primarily in North America. It offers exclusive and non-exclusive brands for men and women.

We need an advertisement design announcing a store opening, to be placed on a hoarding.

A hoarding is a large board in an enclosed shopping center, used to display advertisements; similar to a billboard. It is a temporary board (or fence) erected in front of a retail site during the construction period.

The advertisement we need is to be placed on the hoarding that covers the store front facade during the construction period, and it is removed the night prior to opening day.

Attached are the TREVALLO store pictures, as well as the logo / pantone color document. The primary colors identifying TREVALLO are Rose gold, white, and red.

The objective or focus of the advertisement on the hoarding should include the following:
- TREVALLO (as per logo)
- Opening soon
- website : www.trevallo-example.ca
- Facebook / Twitter
- A clearly identified section of the advertisement announcing that we are recruiting / looking for employees; this should be announced as: "Join the Trevallo Family" and provide email: careers@trevallo-example.ca

Target Market(s)

Women & men between the approx ages of 25 to 65. The age group is quite wide because the product range we have in the store is very diverse too.

Industry/Entity Type

Retail

Requirements
Must have
• 1- Trevallo name / logo
• 2- Opening soon
• 3- website: www.trevallo-example.ca (& Facebook / twitter reference)
• 4- Join the Trevallo Family: careers@trevallo-example.ca
• Main objective: To have a design that will intrigue people walking in a shopping mall enough for them to stop for a second and look at the ad design. (At the end of the day, that's the main objective of a hoarding design - to get people's attention).
Nice to have
• I can give you an approx. SIZE, but I would like a design that can be slightly modified for printing purposes, as the hoarding size from 1 store to the next will not be identical. However, I would like to use the same design for all hoardings.
• With that said, the approx hoarding size would be 15 feet wide and 10 feet high.
• Some other hoardings will be slightly bigger in width (going up to 20 ft max) but the height should be fairly standard.
Should not have
• The end design should not have a picture / design of the store as per the attached images. The store design and how it looks should be a surprise for the customers.

```html
<!DOCTYPE html>
<html lang="en">
<head>
<meta charset="utf-8">
<title>Trevallo — Opening Soon Hoarding</title>
<link href="https://fonts.googleapis.com/css2?family=Exo+2:wght@500;600;800&display=swap" rel="stylesheet">
<style>
  :root {
    --red: #a50303;
    --wine: #9a0a0a;
    --gold-line: #e7b24a;
    --white: #ffffff;
    --page: #ffffff;
  }
  * { margin: 0; padding: 0; box-sizing: border-box; }
  html, body {
    width: 1200px; height: 817px; overflow: hidden;
    background: var(--page);
  }
  .hoarding {
    position: relative; width: 1200px; height: 817px; overflow: hidden;
    font-family: "Exo 2", sans-serif;
  }
  .hoarding__backdrop { position: absolute; inset: 0; }
  .brand-name {
    position: absolute; left: 0; width: 1200px; top: 130px;
    padding-left: 44px;
    text-align: center; color: var(--white);
    font-weight: 500; font-size: 74px; letter-spacing: 44px;
    line-height: 1;
  }
  .headline {
    position: absolute; left: 0; width: 1200px; top: 405px;
    text-align: center; color: var(--wine);
    font-weight: 800; font-size: 100px; letter-spacing: 2px; line-height: 1;
  }
  .contact-list {
    position: absolute; left: 366px; top: 517px; list-style: none;
  }
  .contact-list__item {
    display: flex; align-items: center; height: 58px;
    color: var(--wine); font-weight: 600; font-size: 31px;
  }
  .contact-list__icon {
    width: 38px; height: 38px; margin-right: 32px; flex: none;
  }
  .recruit-band {
    position: absolute; left: 170px; width: 860px; top: 712px; height: 46px;
    background: linear-gradient(90deg, transparent 0%, var(--red) 14%, var(--red) 86%, transparent 100%);
    display: flex; align-items: center; justify-content: center;
    color: var(--white); font-weight: 500; font-size: 22px;
  }
</style>
</head>
<body>
<main class="hoarding">
  <svg class="hoarding__backdrop" width="1200" height="817" viewBox="0 0 1200 817" aria-hidden="true">
    <defs>
      <linearGradient id="red-field" x1="0" y1="0" x2="0" y2="1">
        <stop offset="0" stop-color="#a30000"/>
        <stop offset="1" stop-color="#9a0000"/>
      </linearGradient>
      <linearGradient id="gold-field" x1="0" y1="0" x2="1" y2="0">
        <stop offset="0" stop-color="#9a6413"/>
        <stop offset="0.15" stop-color="#d39b22"/>
        <stop offset="0.45" stop-color="#fff6a0"/>
        <stop offset="0.62" stop-color="#f3c646"/>
        <stop offset="0.85" stop-color="#c98a1c"/>
        <stop offset="1" stop-color="#7a4d0f"/>
      </linearGradient>
      <linearGradient id="gold-shade" x1="0" y1="0" x2="0" y2="1">
        <stop offset="0" stop-color="#5a2a00" stop-opacity="0.35"/>
        <stop offset="0.12" stop-color="#5a2a00" stop-opacity="0"/>
      </linearGradient>
    </defs>
    <rect class="red-field" width="1200" height="817" fill="url(#red-field)"/>
    <g class="trim-lines" stroke="var(--gold-line)" stroke-width="3">
      <line x1="0" y1="67" x2="1200" y2="67"/>
      <line x1="0" y1="248" x2="1200" y2="248"/>
      <line x1="42" y1="0" x2="42" y2="400"/>
      <line x1="140" y1="0" x2="140" y2="400"/>
      <line x1="1055" y1="0" x2="1055" y2="400"/>
      <line x1="1158" y1="0" x2="1158" y2="400"/>
    </g>
    <g class="gold-field" role="img" aria-label="Gold metallic panel with a soft pattern of rounded squares">
      <path d="M0 355 C150 355 250 300 400 295 L800 295 C950 295 1060 315 1200 352 L1200 817 L0 817 Z" fill="url(#gold-field)"/>
      <path d="M0 355 C150 355 250 300 400 295 L800 295 C950 295 1060 315 1200 352 L1200 817 L0 817 Z" fill="url(#gold-shade)"/>
    </g>
  </svg>

  <h1 class="brand-name">TREVALLO</h1>
  <h2 class="headline">OPENING SOON</h2>

  <ul class="contact-list">
    <li class="contact-list__item">
      <svg class="contact-list__icon" viewBox="0 0 38 38" aria-hidden="true">
        <circle cx="19" cy="19" r="18" fill="var(--wine)"/>
        <circle cx="19" cy="19" r="11" fill="none" stroke="var(--white)" stroke-width="2"/>
        <circle cx="19" cy="19" r="4" fill="var(--white)"/>
      </svg>
      www.trevallo-example.ca
    </li>
    <li class="contact-list__item">
      <svg class="contact-list__icon" viewBox="0 0 38 38" aria-hidden="true">
        <circle cx="19" cy="19" r="15" fill="var(--wine)"/>
      </svg>
      #trevallo
    </li>
    <li class="contact-list__item">
      <svg class="contact-list__icon" viewBox="0 0 38 38" aria-hidden="true">
        <rect x="4" y="4" width="30" height="30" fill="var(--wine)"/>
      </svg>
      trevallo-example.ca/community
    </li>
  </ul>

  <p class="recruit-band">Join the Trevallo Family, email resume to: careers@trevallo-example.ca</p>
</main>
</body>
</html>
```